Vodka label for New Brand called HOLT Vodka

We need a label measuring 3.5 inches wide & 5 inches tall for this vodka bottle. The brand is "HOLT Vodka". This should be the largest font on the label. "Handcrafted in the USA" should be on bottle in small font near the bottom. The tagline "Here's Our Liquid Toast" also needs to be included anywhere that makes sense in a smaller font than the brand name. Also in smaller font at the bottom/corners- "80 proof, 750 ml, 40% alc/vol" I value the human mind over AI, but am providing a couple designs that were AI generated to give you a better idea where to start and what we are looking for. Thank you!
Updates

Target Market(s)

21-45 year olds.

Industry/Entity Type

Alcohol

Colors
0054AA
0677BA
7BADD7
CADEEF
E8F1F8
EB3D1F
EC4F4E
F09395
F8D3D4
FCEDEE

Requirements
Should not have
• You can not use the US flag but can use elements of it.

```html
<!DOCTYPE html>
<html lang="en">
<head>
<meta charset="utf-8">
<title>HOLT Vodka Label</title>
<link rel="stylesheet" href="https://fonts.googleapis.com/css2?family=Passion+One:wght@700&family=Montserrat:wght@800&family=Oswald:wght@500;600&display=swap">
<style>
  :root {
    --backdrop: #ebebeb;
    --navy: #13305f;
    --navy-deep: #0c2452;
    --navy-soft: #2d4878;
    --red: #b31d40;
    --white: #ffffff;
  }
  * { margin: 0; padding: 0; box-sizing: border-box; }
  html, body {
    width: 1200px;
    height: 960px;
    overflow: hidden;
    background: var(--backdrop);
  }
  .label {
    position: absolute;
    left: 300px;
    top: 50px;
    width: 600px;
    height: 860px;
    background: var(--white);
    overflow: hidden;
  }
  .star-field {
    position: absolute;
    left: 0; top: 0;
    width: 600px;
    height: 300px;
    background: linear-gradient(100deg, var(--navy-deep) 0%, var(--navy-soft) 45%, var(--navy) 100%);
  }
  .edge-bar {
    position: absolute;
    width: 26px;
    height: 40px;
    background: var(--red);
  }
  .edge-bar.left { left: 0; }
  .edge-bar.right { right: 0; }
  .brand-name {
    position: absolute;
    left: 0; top: 300px;
    width: 600px;
    text-align: center;
    font-family: "Passion One", "Arial Black", sans-serif;
    font-weight: 700;
    font-size: 190px;
    line-height: 1;
    letter-spacing: 4px;
    color: var(--navy);
  }
  .tagline-arc {
    position: absolute;
    left: 0; top: 480px;
    width: 600px;
    height: 90px;
  }
  .tagline-arc text {
    font-family: "Montserrat", sans-serif;
    font-weight: 800;
    font-size: 21px;
    letter-spacing: 2px;
    fill: var(--navy);
  }
  .stripe {
    position: absolute;
    left: 0;
    width: 600px;
    background: var(--red);
    display: flex;
    align-items: center;
    color: var(--white);
    font-family: "Oswald", sans-serif;
    font-weight: 600;
    text-transform: uppercase;
  }
  .stripe-one { top: 580px; height: 56px; }
  .stripe-two { top: 680px; height: 60px; justify-content: center; font-size: 34px; letter-spacing: 1px; }
  .stripe-three { top: 784px; height: 48px; justify-content: space-between; padding: 0 30px; font-size: 26px; }
  .product-banner {
    position: absolute;
    left: 180px; top: 560px;
    width: 240px;
    height: 100px;
  }
  .product-banner text {
    font-family: "Oswald", sans-serif;
    font-weight: 500;
    font-size: 44px;
    letter-spacing: 10px;
    fill: var(--navy);
  }
</style>
</head>
<body>
  <main class="label">
    <div class="star-field" role="img" aria-label="Navy field scattered with white stars"></div>

    <div class="edge-bar left" style="top:340px"></div>
    <div class="edge-bar left" style="top:420px"></div>
    <div class="edge-bar left" style="top:500px"></div>
    <div class="edge-bar right" style="top:320px"></div>
    <div class="edge-bar right" style="top:400px"></div>
    <div class="edge-bar right" style="top:480px"></div>

    <h1 class="brand-name">HOLT</h1>

    <svg class="tagline-arc" viewBox="0 0 600 90" aria-label="Here's Our Liquid Toast">
      <defs>
        <path id="tagline-curve" d="M 60 70 Q 300 10 550 40"/>
      </defs>
      <text><textPath href="#tagline-curve" startOffset="50%" text-anchor="middle">HERE'S OUR LIQUID TOAST</textPath></text>
    </svg>

    <div class="stripe stripe-one"></div>
    <div class="stripe stripe-two">Handcrafted in the USA</div>
    <div class="stripe stripe-three">
      <span class="proof">80 Proof</span>
      <span class="abv">40% Alc/Vol</span>
      <span class="volume">750 ML</span>
    </div>

    <svg class="product-banner" viewBox="0 0 240 100">
      <polygon points="8,4 232,4 232,62 120,96 8,62" fill="var(--white)"/>
      <line x1="4" y1="2" x2="4" y2="66" stroke="var(--navy)" stroke-width="6"/>
      <line x1="236" y1="2" x2="236" y2="66" stroke="var(--navy)" stroke-width="6"/>
      <text x="125" y="58" text-anchor="middle">VODKA</text>
    </svg>
  </main>
</body>
</html>
```